Website redesign for a national printing company

Our current website is dated and boring: ferngladeflags.com

We are looking for a fresh, modern design. We need a clean, minimal design that is also elegant, really shows off large, bright photos of our banners in action and POPS. Our goal is to showcase our beautiful banners, while also giving the user the confidence in our company that we will provide friendly, fast service, fast printing, and deliver their banners on time for their event.

I want a nice flow to the website, the design should tie in well with the printing feel. Here is an example of clean, beautiful design that ties in to the industry - https://www.vorpa.com/ - notice how the buttons are like chat icons, for example.

More examples:

Nice clean design https://www.quilbex.com/

https://tavrimo.com/ nice and clean, but it POPS really well.

I like https://www.prendavel.com/

https://www.ubrato.com/ gorgeous site, clean, modern

Beautiful, simple, clean, modern - https://mirevolta.com/en-us/

These websites are not from the print industry, that’s because most printers don’t have good websites - they are more focused on local businesses, referrals, not really online marketing.

But keep in mind in your design that we need to give the feel that we are printing their banners beautifully, fast, with great service.

https://www.faywendle.com/ so clean, bold, clear to the user what the company does. Love this simple yet elegant design.

https://www.k7.com/ - so pretty! And still so simple and obvious to the user what to do on their site.

https://zulvane.com/

https://quenbrisk.com/us/en/ big and bold - yet super nicely designed with so many nice touches

https://posterlyn.com/ - also clean, simple, and so obvious to the user to take action and contact the company
Updates

I just updated the job brief, and you can also view it in full here - https://files.oskavimo.com/document/d/7Hrp2LmQz94VtNcXe0BgYsJd1KwFu63aPoE8iRnCTyUZ/edit?usp=sharing

Target Market(s)

Please read this customer persona - https://files.oskavimo.com/document/d/7Hrp2LmQz94VtNcXe0BgYsJd1KwFu63aPoE8iRnCTyUZ/edit?usp=sharing

Industry/Entity Type

Printing

Number of Pages Required

1 page

Requirements
Must have
• Nice flow to the website, the design should tie in well with the printing feel. Here is an example of clean, beautiful design that ties in to the industry - https://www.vorpa.com/ - notice how the buttons are like chat icons, for example.
Should not have
• No filters on the images, we want large, beautiful images.

```html
<!DOCTYPE html>
<html lang="en">
<head>
<meta charset="utf-8">
<title>Fernglade Flags — Banner Printing</title>
<link href="https://fonts.googleapis.com/css2?family=Fira+Sans:wght@400;500&family=Poppins:wght@400;500;600&display=swap" rel="stylesheet">
<style>
:root{
  --blue:#1a4dbb;
  --blue-deep:#1443a8;
  --blue-bright:#2b63dc;
  --navy:#02143a;
  --ink:#2b2f3a;
  --muted:#6b7080;
  --pale:#eef3fd;
  --pale-band:#e3eaf7;
  --gray-box:#f2f2f2;
  --white:#ffffff;
  --gold:#ffc414;
}
*{box-sizing:border-box;margin:0;padding:0}
html,body{width:1200px;height:1200px;overflow:hidden;background:var(--white)}
body{font-family:"Poppins",sans-serif;color:var(--ink)}
h1,h2,h3,h4,h5{font-weight:400}
.canvas{position:relative;width:1200px;height:1200px;overflow:hidden;background:var(--white)}
.page{position:absolute;left:369.5px;top:0;width:742px;height:1932px;transform:scale(0.6211);transform-origin:0 0;overflow:hidden;background:var(--white)}
.abs{position:absolute}
.heading{font-family:"Fira Sans",sans-serif;font-weight:400}
.blue{color:var(--blue)}
.btn{position:absolute;display:flex;align-items:center;justify-content:center;border-radius:12px;font-size:6.5px;font-family:"Poppins",sans-serif;white-space:nowrap}
.btn-solid{background:var(--blue);color:var(--white)}
.btn-line{border:1px solid var(--blue);color:var(--blue);background:var(--white)}
.deco{position:absolute;left:0;top:0}

/* top bar & header */
.topbar{left:92px;top:0;width:557px;height:16px;background:var(--blue);border-radius:0 0 8px 8px;color:var(--white);font-size:5.5px}
.topbar .dot{position:absolute;top:5px;width:6px;height:6px;border-radius:50%;background:var(--white)}
.topbar .contact{position:absolute;right:18px;top:4px}
.hero-bg{left:0;top:0;width:742px;height:345px;background:var(--pale)}
.logo{left:98px;top:29px}
.logo .name{font-family:"Fira Sans",sans-serif;font-size:15px;color:var(--blue);font-weight:500;line-height:1}
.logo .sub{font-size:5.5px;letter-spacing:4px;color:var(--blue);margin-left:20px;margin-top:1px}
.nav{top:38px;font-size:7px;color:var(--ink)}

/* hero */
.hero-kicker{left:98px;top:115px;font-size:13px;color:var(--blue)}
.hero-title{left:97px;top:128px;font-size:37px;color:var(--ink);letter-spacing:.3px;white-space:nowrap}
.hero-text{left:99px;top:178px;width:225px;font-size:6.4px;line-height:11.4px;color:var(--ink)}
.hero-more{left:99px;top:270px;font-size:6.5px}
.hero-more b{color:var(--blue);font-weight:600;margin-left:3px}

/* clients */
.clients-box{left:0;top:375px;width:203px;height:88px;background:var(--gray-box);border-radius:0 6px 6px 0}
.clients-title{left:105px;top:403px;font-size:12.5px;line-height:16px}
.arrow-dot{position:absolute;width:14px;height:14px;border-radius:50%;background:var(--ink)}
.arrow-dot::after{content:"";position:absolute;left:11px;top:6.5px;width:9px;height:1px;background:var(--ink)}
.client{top:408px;font-family:"Fira Sans",sans-serif;color:#4a4d55;font-weight:500;white-space:nowrap}

/* products */
.section-mark{width:15px;height:18px;background:var(--blue)}
.section-title{font-size:13px;color:var(--blue);white-space:nowrap}
.card{position:absolute;top:532px;width:126px;height:209px;border:1px solid var(--blue);border-radius:6px;background:var(--white);padding:12px 7px}
.card .icon{width:48px;height:40px;background:#e6e9ef;border-radius:3px}
.card h3{font-family:"Fira Sans",sans-serif;font-weight:400;font-size:8.3px;color:var(--blue);line-height:11px;margin-top:17px;margin-bottom:5px}
.card p{font-size:5.6px;line-height:9.3px;color:#4a4d55}
.card .learn{position:absolute;left:7px;bottom:16px;font-size:5.6px;display:flex;align-items:center;gap:4px}
.card .learn i{display:inline-block;width:9px;height:9px;border-radius:50%;background:var(--blue)}

/* contact / upload */
.tab{top:809px;font-size:5.8px;line-height:10px;color:#4a4d55}
.tab.active::before,.tab.active::after{content:"";position:absolute;left:0;width:35px;height:1.5px;background:var(--blue)}
.tab.active::before{top:-5px}.tab.active::after{bottom:-6px}
.photo{position:absolute;border-radius:6px}
.form{left:376px;top:849px;width:267px;height:181px;border:1px solid var(--blue);border-radius:6px;background:var(--white)}
.form h3{position:absolute;left:11px;top:16px;font-family:"Fira Sans",sans-serif;font-weight:400;font-size:12.5px}
.field{position:absolute;font-size:5.8px;border-bottom:1px solid #9aa3b5;padding-bottom:5px}

/* newsletter */
.newsletter{left:0;top:1062px;width:742px;height:59px;background:var(--navy)}
.nl-input{left:262px;top:20px;width:160px;height:19px;background:var(--white);border-radius:10px 0 0 10px;font-size:6.2px;padding:6px 11px;color:#555}
.nl-btn{left:422px;top:20px;width:57px;height:19px;border-radius:0 10px 10px 0}

/* testimonial */
.testi{left:0;top:1121px;width:742px;height:237px;overflow:hidden;background:linear-gradient(120deg,#1a49c0,#2a66e0 55%,#1a49c0)}
.testi-name{left:338px;top:55px;font-family:"Fira Sans",sans-serif;font-size:9.5px;color:var(--white)}
.testi-quote{left:338px;top:90px;width:200px;font-size:5.8px;line-height:11.6px;color:var(--white)}
.round{position:absolute;width:14px;height:14px;border-radius:50%;background:var(--white)}

/* blogs */
.blogs-title{left:0;top:1385px;width:742px;text-align:center;font-family:"Fira Sans",sans-serif;font-weight:400;font-size:13px}
.blogs-text{left:230px;top:1410px;width:282px;text-align:center;font-size:5.8px;line-height:8.4px;color:#4a4d55}
.blog{position:absolute;top:1457px;width:158px;height:197px;border:1px solid var(--blue);border-radius:6px;background:var(--white);overflow:hidden}
.blog .img{height:103px;background:linear-gradient(135deg,#3b4a5e,#8a97a8 60%,#d8c9b4)}
.blog .year{position:absolute;right:0;top:92px;background:var(--blue);color:var(--white);font-size:6px;padding:1px 6px;border-radius:5px 0 0 0}
.blog h4{font-family:"Fira Sans",sans-serif;font-weight:400;font-size:8.3px;margin:10px 8px 6px}
.blog p{font-size:5.8px;line-height:9.3px;color:#4a4d55;margin:0 8px}
.blog .meta{position:absolute;left:8px;right:6px;bottom:19px;display:flex;justify-content:space-between;font-size:5.8px;color:#4a4d55}
.date{position:absolute;top:1441px;width:30px;height:31px;background:var(--blue);border-radius:6px;color:var(--white);text-align:center}
.date b{display:block;font-family:"Fira Sans",sans-serif;font-weight:500;font-size:17px;line-height:20px}
.date span{display:block;font-size:4px;line-height:4px}

/* footer */
.footer{left:0;top:1718px;width:742px;height:214px;background:var(--blue);color:var(--white);overflow:hidden}
.footer h5{font-family:"Fira Sans",sans-serif;font-weight:400;font-size:8.5px;margin-bottom:8px}
.footer ul{list-style:none;font-size:6px;line-height:14px}
.fcol{position:absolute;top:37px}
.finfo{font-size:5.8px;line-height:14px}
.copyright{position:absolute;left:0;bottom:0;width:742px;height:15px;background:#0e3590;font-size:5px;padding:5px 98px}
.social{position:absolute;top:140px;width:8px;height:8px;border-radius:50%;background:var(--white)}
</style>
</head>
<body>
<div class="canvas">
<main class="page">

  <!-- background bands -->
  <div class="abs hero-bg"></div>
  <svg class="deco" width="742" height="1932" viewBox="0 0 742 1932">
    <polygon points="655,345 742,345 742,430" fill="var(--pale-band)"/>
    <polygon points="742,430 742,520 0,1065 0,980" fill="var(--pale-band)"/>
    <polygon points="580,440 742,440 742,470 0,1060 0,960" fill="var(--pale-band)" opacity=".8"/>
    <polygon points="0,1358 120,1358 420,1718 330,1718" fill="var(--pale-band)"/>
  </svg>

  <!-- top bar -->
  <div class="abs topbar">
    <span class="dot" style="left:18px"></span><span class="dot" style="left:31px"></span><span class="dot" style="left:44px"></span><span class="dot" style="left:57px"></span>
    <span class="contact">Toll Free: 800-555-0142 &nbsp;&nbsp; info@ferngladeflags.com</span>
  </div>

  <!-- header -->
  <div class="abs logo"><div class="name">Fernglade Flags</div><div class="sub">BANNERS</div></div>
  <span class="abs nav" style="left:398px">About</span>
  <span class="abs nav" style="left:430px">Products ˅</span>
  <span class="abs nav" style="left:478px">Galleries ˅</span>
  <div class="btn btn-solid" style="left:526px;top:32px;width:49px;height:20px;border-radius:10px;font-size:7px">Upload</div>
  <div class="btn btn-solid" style="left:583px;top:32px;width:60px;height:20px;border-radius:10px;font-size:7px">Get Quote</div>

  <!-- hero -->
  <div class="abs heading hero-kicker">Festival &amp; Event, Plastic Roll, Large Format</div>
  <h1 class="abs heading hero-title">Banner Printing</h1>
  <p class="abs hero-text">For over two decades, Fernglade Flags has been the go-to source for high-quality custom printing for large format banners, plastic roll banners, stage backdrops and mobile stage festival banners.</p>
  <div class="btn btn-solid" style="left:99px;top:237px;width:54px;height:19px">Know More</div>
  <div class="btn btn-line" style="left:165px;top:237px;width:56px;height:19px">Contact Us</div>
  <p class="abs hero-more">Check More at: <b>stagecurtainhub.com</b></p>
  <svg class="abs" style="left:370px;top:86px" width="270" height="226" viewBox="0 0 270 226">
    <defs><linearGradient id="heroG" x1="0" y1="0" x2="1" y2="1"><stop offset="0" stop-color="#2a4b9a"/><stop offset="1" stop-color="#101a3a"/></linearGradient></defs>
    <path d="M30,45 C60,10 140,-8 200,8 C255,22 268,90 250,150 C232,205 170,232 110,214 C60,198 10,150 18,100 C21,80 24,58 30,45Z" fill="var(--white)" stroke="var(--blue)" stroke-width="3"/>
    <path d="M55,30 L195,22 L238,60 L238,170 L150,196 L5,175 L8,95 Z" fill="url(#heroG)" role="img" aria-label="Photo of a mobile stage building wrapped in printed blue mesh banners"/>
  </svg>

  <!-- clients -->
  <div class="abs clients-box"></div>
  <div class="abs heading clients-title">Our Awesome<br><span class="blue">Clients</span></div>
  <span class="arrow-dot" style="left:196px;top:413px"></span>
  <span class="client abs" style="left:245px;font-size:19px">Korvana</span>
  <span class="client abs" style="left:360px;top:414px;font-size:9px">Radiowell Media</span>
  <span class="client abs" style="left:466px;top:413px;font-size:9px">Baylen Comets</span>
  <span class="client abs" style="left:562px;top:417px;font-size:13px;font-weight:400">Stratova</span>
  <span class="arrow-dot" style="left:652px;top:413px"></span>

  <!-- products -->
  <span class="abs section-mark" style="left:98px;top:495px"></span>
  <h2 class="abs heading section-title" style="left:120px;top:496px">Our Products</h2>
  <article class="card" style="left:98px">
    <div class="icon" role="img" aria-label="Line icon of a rolled plastic banner"></div>
    <h3>Plastic Roll Banners</h3>
    <p>Plastic Roll Banners offer an economical and effective way to communicate your marketing message at concerts, sporting events, radio station events, motor sports events, political rallies, and anywhere else groups of people gather. Printed on 4 mil or 6 mil low density polyethylene, they are easily recyclable and biodegradable.</p>
    <span class="learn">Learn More <i></i></span>
  </article>
  <article class="card" style="left:237px">
    <div class="icon" role="img" aria-label="Line icon of a festival sign"></div>
    <h3>Festival Banners and Stage Backdrops</h3>
    <p>Great for large backdrops and stage scrims at outdoor festivals or concerts. The mesh allows for air to flow through the banner, for maximum visual effect and sound flow. The scrims on either side of the stage offer privacy to the stage hands and upcoming valued performers.</p>
    <span class="learn">Learn More <i></i></span>
  </article>
  <article class="card" style="left:375px">
    <div class="icon" role="img" aria-label="Line icon of a mesh grid"></div>
    <h3>Large Format and Mesh Banners</h3>
    <p>Transform any space with your brand on mesh banners. Digitally printed and fully customizable, mesh banners are optimal for outdoor use. Air flow and durability make vinyl mesh ideal for fencing, speaker mesh, stage mesh, building wraps and any other huge banner.</p>
    <span class="learn">Learn More <i></i></span>
  </article>

  <!-- contact & upload -->
  <span class="abs section-mark" style="left:98px;top:774px"></span>
  <h2 class="abs heading section-title" style="left:121px;top:775px">Contact and Make Your Artworks Live</h2>
  <span class="abs tab" style="left:99px">Plastic Roll<br>Banners Gallery</span>
  <span class="abs tab" style="left:194px">Large Format/<br>Mesh Banners Gallery</span>
  <span class="abs tab active" style="left:284px">Festival/Stage<br>Backdrops Gallery</span>
  <div class="photo" style="left:97px;top:849px;width:266px;height:181px;background:linear-gradient(160deg,#5a2a7a,#1c2a55 40%,#b04a3a 75%,#30203a)" role="img" aria-label="Concert crowd in front of a festival stage dressed with printed backdrops"></div>
  <span class="round" style="left:115px;top:933px;opacity:.85"></span>
  <span class="round" style="left:333px;top:933px;opacity:.85"></span>

  <h2 class="abs heading section-title" style="left:375px;top:775px">Are you a Band?</h2>
  <p class="abs" style="left:376px;top:799px;font-size:5.8px">Contact our product experts for all your pricing and sizing needs.</p>
  <p class="abs heading blue" style="left:376px;top:815px;font-size:13px">STAGECURTAINHUB.COM</p>
  <span class="abs" style="left:557px;top:816px;width:15px;height:15px;border-radius:50%;background:var(--blue)"></span>

  <section class="abs form">
    <h3>Upload Your <span class="blue">Art Work</span></h3>
    <span class="field" style="left:12px;top:48px;width:115px">Your Name</span>
    <span class="field" style="left:140px;top:48px;width:115px">Email Address</span>
    <span class="field" style="left:12px;top:73px;width:115px">Contact Number</span>
    <span class="field" style="left:140px;top:73px;width:115px">Company Name</span>
    <span class="field" style="left:12px;top:98px;width:243px;padding-bottom:18px">Message - Please put details here</span>
    <div class="btn btn-solid" style="left:10px;top:140px;width:57px;height:21px;border-radius:11px">Upload File</div>
    <div class="btn btn-solid" style="left:78px;top:140px;width:54px;height:21px;border-radius:11px">Send Query</div>
  </section>

  <!-- newsletter -->
  <section class="abs newsletter">
    <div class="abs nl-input">Enter Email &amp; Join With Us</div>
    <div class="btn btn-solid nl-btn" style="font-size:6.5px">Subscribe</div>
  </section>

  <!-- testimonial -->
  <section class="abs testi">
    <svg class="deco" width="742" height="237" viewBox="0 0 742 237">
      <polygon points="0,28 0,45 130,237 148,237" fill="var(--white)"/>
      <polygon points="562,0 578,0 712,237 696,237" fill="var(--white)"/>
      <circle cx="255" cy="119" r="82" fill="none" stroke="#ffffff" stroke-opacity=".15"/>
    </svg>
    <div class="abs" style="left:193px;top:33px;width:124px;height:175px;border-radius:50%;background:linear-gradient(180deg,#c9d3e2,#27407a 70%,#1a2c58)" role="img" aria-label="Portrait of the customer giving the review"></div>
    <span class="round" style="left:511px;top:35px"></span>
    <span class="round" style="left:534px;top:35px"></span>
    <div class="abs testi-name">Marisol T</div>
    <div class="abs" style="left:338px;top:69px;font-size:10px;color:var(--gold);letter-spacing:1px">★★★★★</div>
    <p class="abs testi-quote">"Fernglade was great to work with. We used them to make banners for our outdoor graduation in our city. They assisted with artwork, were super responsive, and had quick shipping."</p>
    <p class="abs" style="left:338px;top:136px;font-size:6.2px;font-weight:600;color:var(--white)">2 months ago</p>
    <div class="btn" style="left:338px;top:161px;width:72px;height:19px;background:var(--white);color:var(--blue);border-radius:10px">All Testimonials</div>
  </section>

  <!-- blogs -->
  <h2 class="abs blogs-title">Check our recent <span class="blue">Blogs</span></h2>
  <p class="abs blogs-text">You can check our all latest news, movements, projects, post works not only these we also cover technical news from all over the world for our tech savvies.</p>

  <article class="blog" style="left:114px">
    <div class="img" role="img" aria-label="Photo of a designer working on a laptop"></div><span class="year">2023</span>
    <h4>Why we maintain RGB/CMYK</h4>
    <p>Lorem ipsum dolor sit amet, consectetur adipiscing elit, sed do eiusmod tempor incididunt ut labore et dolore magna aliqua.</p>
    <div class="meta"><span>● Daniel Ortiz</span><span>▭ Read More</span></div>
  </article>
  <article class="blog" style="left:299px">
    <div class="img" style="background:linear-gradient(135deg,#d9d4cc,#7a6a5a 50%,#e8e2d8)" role="img" aria-label="Photo of hands reviewing color swatches"></div><span class="year">2023</span>
    <h4>Choosing color matters</h4>
    <p>Lorem ipsum dolor sit amet, consectetur adipiscing elit, sed do eiusmod tempor incididunt ut labore et dolore magna aliqua.</p>
    <div class="meta"><span>● Daniel Ortiz</span><span>▭ Read More</span></div>
  </article>
  <article class="blog" style="left:485px">
    <div class="img" role="img" aria-label="Photo of a designer working on a laptop"></div><span class="year">2023</span>
    <h4>Design Makes Difference</h4>
    <p>Lorem ipsum dolor sit amet, consectetur adipiscing elit, sed do eiusmod tempor incididunt ut labore et dolore magna aliqua.</p>
    <div class="meta" style="bottom:21px"><span>● Daniel Ortiz</span><span>▭ Read More</span></div>
  </article>
  <div class="date" style="left:98px"><b>12</b><span>September</span></div>
  <div class="date" style="left:283px"><b>26</b><span>June</span></div>
  <div class="date" style="left:469px"><b>30</b><span>August</span></div>
  <div class="btn btn-solid" style="left:332px;top:1670px;width:78px;height:16px;border-radius:8px;font-size:7px">Check All Blogs</div>

  <!-- footer -->
  <footer class="abs footer">
    <svg class="deco" width="742" height="214" viewBox="0 0 742 214">
      <polygon points="22,0 70,0 180,214 132,214" fill="#ffffff" opacity=".1"/>
      <polygon points="582,0 628,0 742,180 742,214 708,214" fill="var(--white)"/>
    </svg>
    <div class="fcol" style="left:98px"><h5>Company</h5><ul><li>About us</li><li>Reviews</li><li>Contact Us</li><li>Privacy Policy</li><li>Blog</li></ul></div>
    <div class="fcol" style="left:191px"><h5>Information</h5><ul><li>Request a Catalog</li><li>Articles</li><li>FAQ</li><li>Customer Reviews</li><li>Customer Sales</li></ul></div>
    <div class="fcol" style="left:283px"><h5>Important</h5><ul><li>Get a Quote</li><li>Upload</li><li>Pay</li><li>Contact Us</li></ul></div>
    <div class="fcol" style="left:376px;width:130px"><h5>Subscribe &amp; Contact</h5><p style="font-size:5.8px;line-height:7px">Get discounts, promotions, blog posts and news straight to your inbox. We don't spam!</p></div>
    <div class="abs" style="left:376px;top:91px;width:112px;height:19px;background:var(--white);border-radius:10px;color:#555;font-size:6px;padding:6px 12px">Your Email</div>
    <div class="btn" style="left:492px;top:91px;width:57px;height:19px;background:var(--white);color:var(--blue);border-radius:10px">Subscribe</div>
    <div class="abs finfo" style="left:376px;top:117px">
      <p>⌖ &nbsp;1870 Larkspur Ct, Millbrook, MI 48199, USA</p>
      <p>✆ &nbsp;(Local &amp; Canada - 800-555-0142 / 734-555-0187</p>
      <p>✆ &nbsp;Toll Free: 800-555-0142</p>
      <p>✉ &nbsp;Email Us - info@ferngladeflags.com</p>
    </div>
    <span class="social" style="left:98px"></span><span class="social" style="left:116px"></span><span class="social" style="left:134px"></span><span class="social" style="left:152px"></span>
    <div class="copyright">Copyright © 2023 Fernglade Flags - All Rights Reserved.</div>
  </footer>

</main>
</div>
</body>
</html>
```